Need a new logo/business card for a cafe

I need a new logo and business card for a café. The café is called "Ladle", and we have a reputation for making a high quality cup of espresso coffee. I would like the business card design to reflect this "high quality". Our baristas craft our customers coffee with care to achieve this result. I would like to see designs that include a warm latte brown color. The card will be single sided to allow the rear to be used as a loyalty card which means the design will need to include space for our business address, phone number, and facebook page details. The uploaded logo is already in use on the café front window, and if it can be incorporated or used that would be great, but I am open to completely new designs as well. Thank you.
Updates
Thank you to all for the submissions. There's quite a few I like now, the hardest part will be choosing! I've set up a poll for added feedback from my own contacts and will wait on results from that.
Hello, more great designs coming in, thank you very much. There's quite a few that I really like, so my biggest challenge is going to be choosing one. Thanks again for your time, and I'll get onto the hard task of making that choice. Marisa
Industry/Entity Type
Cafe
Look and feel
Each slider illustrates characteristics of the customer's brand and the style your logo design should communicate.

```html
<!DOCTYPE html>
<html lang="en">
<head>
<meta charset="utf-8">
<title>Ladle – Business Card</title>
<link href="https://fonts.googleapis.com/css2?family=Nothing+You+Could+Do&display=swap" rel="stylesheet">
<style>
  :root {
    --card-white: #ffffff;
    --splash-beige: #ebe4de;
    --latte-brown: #8c7064;
    --wordmark-brown: #8a7066;
    --espresso-dark: #7a3f1c;
    --cup-brown: #8b5a3c;
    --ink-black: #141414;
    --band-text: #f7f1ec;
  }
  html, body {
    margin: 0;
    padding: 0;
    overflow: hidden;
    background: var(--card-white);
  }
  .business-card {
    position: relative;
    width: 1200px;
    height: 686px;
    overflow: hidden;
    background: var(--card-white);
    font-family: "Nothing You Could Do", cursive;
  }
  .background-splash {
    position: absolute;
    left: 0;
    top: 0;
    width: 1200px;
    height: 523px;
    background:
      radial-gradient(ellipse at 60% 35%, rgba(235,228,222,0.9) 0%, rgba(235,228,222,0.35) 45%, rgba(255,255,255,0) 75%),
      radial-gradient(ellipse at 25% 70%, rgba(235,228,222,0.6) 0%, rgba(255,255,255,0) 60%);
  }
  .cup-illustration {
    position: absolute;
    left: 38px;
    top: 14px;
    width: 360px;
    height: 490px;
    border-radius: 40% 40% 30% 30% / 30% 30% 20% 20%;
    background: linear-gradient(160deg, var(--cup-brown) 0%, var(--espresso-dark) 100%);
    opacity: 0.85;
  }
  .wordmark {
    position: absolute;
    left: 590px;
    top: 40px;
    margin: 0;
    font-size: 150px;
    font-weight: 400;
    line-height: 1;
    color: var(--wordmark-brown);
  }
  .address {
    position: absolute;
    left: 470px;
    top: 318px;
    margin: 0;
    font-style: normal;
    font-size: 58px;
    line-height: 66px;
    color: var(--ink-black);
  }
  .contact-band {
    position: absolute;
    left: 0;
    top: 523px;
    width: 1200px;
    height: 163px;
    background: var(--latte-brown);
  }
  .contact-phone,
  .contact-web {
    position: absolute;
    top: 52px;
    margin: 0;
    font-size: 44px;
    line-height: 1;
    color: var(--band-text);
  }
  .contact-phone { left: 74px; }
  .contact-web { right: 108px; }
</style>
</head>
<body>
  <main class="business-card">
    <div class="background-splash" role="img" aria-label="Soft beige paint splatter texture across the card background"></div>
    <div class="cup-illustration" role="img" aria-label="Illustration of a brown coffee cup with a swirl of steam rising above it"></div>
    <h1 class="wordmark">Ladle</h1>
    <address class="address">48 Roastery Row<br>Bramwell, NY 14820</address>
    <footer class="contact-band">
      <p class="contact-phone">(555) 013-2847</p>
      <p class="contact-web">ladlecafe.net</p>
    </footer>
  </main>
</body>
</html>
```